Hollow Fern Kentucky Bourbon Whiskey

We need a label design for a bottle of whiskey. It is for a 750 ml bottle and needs to have a place to write in proof, age, and bottle number at bottom of label. It is a single barrel bourbon. We want to include our tree logo attached in the upload files in some way. Leave out the Distillery part to where it just says Hollow Fern Bourbon Whiskey with the tree. We need the label to be clean and modern. I have also attached a picture of the bottle the label is intended to go on.

Industry/Entity Type

Bourbon

Requirements
Must have
• Hollow Fern tree from file

```html
<!DOCTYPE html>
<html lang="en">
<head>
<meta charset="utf-8">
<title>Hollow Fern Bourbon Whiskey – Label</title>
<link href="https://fonts.googleapis.com/css2?family=Marcellus&family=Bebas+Neue&family=Roboto+Condensed:wght@700&family=Mrs+Saint+Delafield&display=swap" rel="stylesheet">
<style>
  :root {
    --page: #ffffff;
    --label: #000000;
    --gold: #c08f26;
    --white: #ffffff;
  }
  * { margin: 0; padding: 0; box-sizing: border-box; }
  html, body {
    width: 1200px;
    height: 1024px;
    overflow: hidden;
    background: var(--page);
  }
  .label {
    position: absolute;
    left: 275px;
    top: 65px;
    width: 650px;
    height: 894px;
    background: var(--label);
    color: var(--white);
    text-align: center;
  }
  .rule {
    position: absolute;
    left: 0;
    width: 100%;
    height: 3px;
    background: var(--gold);
  }
  .rule--top { top: 78px; }
  .rule--bottom { top: 812px; }

  .brand {
    position: absolute;
    top: 150px;
    left: 0;
    width: 100%;
    display: flex;
    flex-direction: column;
    align-items: center;
    gap: 26px;
  }
  .brand__dot {
    width: 96px;
    height: 96px;
    border-radius: 50%;
    background: var(--gold);
  }
  .brand__name {
    font-family: "Marcellus", serif;
    font-size: 54px;
    letter-spacing: 0.04em;
    color: var(--gold);
    text-transform: uppercase;
  }

  .style-line {
    position: absolute;
    top: 448px;
    width: 100%;
    font-family: "Mrs Saint Delafield", cursive;
    font-size: 48px;
    color: var(--gold);
  }
  .spirit {
    position: absolute;
    top: 522px;
    width: 100%;
    font-family: "Bebas Neue", sans-serif;
    font-size: 50px;
    letter-spacing: 0.32em;
    padding-left: 0.32em;
  }
  .age {
    position: absolute;
    top: 590px;
    width: 100%;
    display: flex;
    justify-content: center;
    align-items: center;
    gap: 8px;
    font-family: "Marcellus", serif;
    font-size: 38px;
    color: var(--gold);
  }
  .age__number {
    width: 56px;
    height: 56px;
    border: 2px solid var(--gold);
    border-radius: 50%;
    display: flex;
    align-items: center;
    justify-content: center;
    font-size: 40px;
    line-height: 1;
  }
  .details {
    position: absolute;
    top: 670px;
    width: 100%;
    font-family: "Roboto Condensed", sans-serif;
    font-weight: 700;
    font-size: 26px;
    letter-spacing: 0.06em;
    line-height: 40px;
  }
  .details__volume { font-size: 28px; margin-top: 6px; }
</style>
</head>
<body>
  <main class="label">
    <div class="rule rule--top"></div>

    <div class="brand">
      <span class="brand__dot"></span>
      <span class="brand__name">Hollow Fern</span>
    </div>

    <p class="style-line">Original Straght</p>
    <h1 class="spirit">Bourbon Whiskey</h1>
    <p class="age"><span>AGED</span><span class="age__number">5</span><span>YEARS</span></p>

    <div class="details">
      <p class="details__bottle">BOTTLE NO. 0017</p>
      <p class="details__proof">45.2% ALC/VOL (90.4 PROOF)</p>
      <p class="details__volume">750ml</p>
    </div>

    <div class="rule rule--bottom"></div>
  </main>
</body>
</html>
```